Design NEW business card

We would like a business card using the colour deep red wine or dark navy blue textured background (patterned or not, open to suggestions) with a high gloss debossed rose gold/copper MT Martin Tully Jewellery business name (Provided). I have included images for your review we would like to keep our currently logo and business name on the front but you can change the layout and positioning. For the back of the card we are open to all suggestions/variations.
Industry/Entity Type
Business
Contact Information for Business Card
Use our current MT Martin Tully Jewellery logo (Provided image)
Look and feel
Each slider illustrates characteristics of the customer's brand and the style your logo design should communicate.

```html
<!DOCTYPE html>
<html lang="en">
<head>
<meta charset="utf-8">
<title>Martin Tully Jewellery – Business Card</title>
<link rel="stylesheet" href="https://fonts.googleapis.com/css2?family=Open+Sans:wght@400;600&display=swap">
<style>
  :root {
    --backdrop: #2b2624;
    --wine: #5e2229;
    --wine-deep: #4f1c22;
    --rose-gold: #c99478;
    --ink-light: #f3ece8;
    --rule: #efe6e2;
  }
  * { margin: 0; padding: 0; box-sizing: border-box; }
  html, body { width: 1200px; height: 864px; overflow: hidden; }
  body {
    background: var(--backdrop);
    font-family: "Open Sans", Arial, sans-serif;
    position: relative;
  }
  .card {
    position: absolute;
    background: linear-gradient(160deg, var(--wine) 0%, var(--wine-deep) 100%);
    box-shadow: 0 10px 24px rgba(0,0,0,.45);
    color: var(--ink-light);
  }
  .card--front { left: 70px; top: 80px; width: 500px; height: 286px; }
  .card--back  { left: 600px; top: 420px; width: 540px; height: 309px; }

  .wordmark {
    position: absolute;
    color: var(--rose-gold);
    font-weight: 400;
    text-transform: uppercase;
    letter-spacing: .22em;
    line-height: 1.35;
    text-align: center;
    display: flex;
    align-items: center;
    gap: 12px;
  }
  .wordmark__dot {
    width: 14px; height: 14px; border-radius: 50%;
    background: var(--rose-gold);
    flex: none;
  }
  .card--front .wordmark { left: 110px; top: 98px; font-size: 20px; }
  .card--front .wordmark small { display: block; font-size: 11px; letter-spacing: .55em; }
  .front__web {
    position: absolute; left: 0; right: 0; top: 200px;
    text-align: center; font-size: 14px; letter-spacing: .3em;
    color: var(--rose-gold);
  }

  .person { position: absolute; left: 26px; top: 46px; }
  .person__name { font-size: 15px; font-weight: 600; color: var(--rose-gold); letter-spacing: .03em; }
  .person__role { font-size: 12px; color: var(--ink-light); }
  .contacts { position: absolute; left: 26px; top: 96px; list-style: none; font-size: 12.5px; line-height: 19px; }
  .contacts li { display: flex; align-items: center; gap: 8px; }
  .contacts svg { width: 11px; height: 11px; fill: var(--rose-gold); flex: none; }
  .rule { position: absolute; height: 1px; background: var(--rule); }
  .rule--mid { left: 26px; right: 0; top: 134px; }
  .rule--low { right: 26px; width: 200px; top: 226px; }
  .card--back .wordmark { left: 290px; top: 90px; font-size: 18px; }
  .card--back .wordmark small { display: block; font-size: 10px; letter-spacing: .55em; }
  .address { position: absolute; right: 26px; top: 236px; text-align: right; font-size: 13px; line-height: 18px; }
  .address__web { letter-spacing: .06em; }
</style>
</head>
<body>
  <section class="card card--front" aria-label="Card front">
    <div class="wordmark">
      <span class="wordmark__dot"></span>
      <span>Martin Tully<small>Jewellery</small></span>
    </div>
    <p class="front__web">www.martintully.com</p>
  </section>

  <section class="card card--back" aria-label="Card back">
    <div class="person">
      <p class="person__name">OWEN HARTLEY</p>
      <p class="person__role">CEO/FOUNDER</p>
    </div>
    <ul class="contacts">
      <li><svg viewBox="0 0 12 12"><path d="M1 4c0-2 2-3 5-3s5 1 5 3l-2 1-1-1.5H4L3 5zM2 6h8l1 5H1z"/></svg>555 310 2468</li>
      <li><svg viewBox="0 0 12 12"><path d="M3.5 0h5a1 1 0 0 1 1 1v10a1 1 0 0 1-1 1h-5a1 1 0 0 1-1-1V1a1 1 0 0 1 1-1zM4 1.5v8h4v-8z"/></svg>555 742 1093</li>
      <li><svg viewBox="0 0 12 12"><path d="M3 0h6v4H3zM1 5h10v5H9v2H3v-2H1zM4 8v3h4V8z"/></svg>555 908 3615</li>
      <li><svg viewBox="0 0 12 12"><path d="M0 2h12v1L6 7 0 3zM0 4.5l6 4 6-4V10H0z"/></svg>hello@martintully.com</li>
    </ul>
    <div class="rule rule--mid"></div>
    <div class="wordmark">
      <span class="wordmark__dot"></span>
      <span>Martin Tully<small>Jewellery</small></span>
    </div>
    <div class="rule rule--low"></div>
    <address class="address" style="font-style:normal">
      214 Alder Crest Way<br>
      Fairview, Oregon 97024<br>
      <span class="address__web">www.martintully.com</span>
    </address>
  </section>
</body>
</html>
```